Magento e-commerce webdesign

We need a full e-commerce design for a company based in France. The website will sell belts (men / women).
In files, you have our logo. We made a try for a brown visit card, but it's just an idea. The brown color can be used if it looks like leather, warning it MUSN'T look like "brown shit" :)
So you are free with color but never forget we sell belts and it's both for men & women (upmarket). You can make your own colors changes on the logo (only colors).
You'll find 2 wireframes with the home page & the category page. Elements are in french. UPDATED : you have a traduction files, but it would better if you can make it in french.
Photos have to be on a white background.
Carroussel & every pictures of the wireframes area are very importants.
Target Market(s)
Men & women
Fashion peoples
Upmarket
Industry/Entity Type
It Company
Requirements
Must have
- work on the colors
- work on the pictures (carroussel, newsletter, ventes privées, services, category)
- pro & upmarket
Nice to have
- Product detail page
- Texts in french
Should not have
- Shitty brown colors

```html
<!DOCTYPE html>
<html lang="fr">
<head>
<meta charset="utf-8">
<title>Sanglea – Liste des produits</title>
<link href="https://fonts.googleapis.com/css2?family=Arimo:wght@400;700&family=Lora:ital,wght@0,400;0,700;1,400;1,700&display=swap" rel="stylesheet">
<style>
:root{
  --purple:#7b5b80;
  --leather:#5b3f2f;
  --leather-dark:#3e2a1f;
  --beige:#b8a58e;
  --blue:#8fb5da;
  --grey-bg:#ececec;
  --line:#dcdcdc;
  --text:#444;
  --muted:#777;
  --white:#fff;
}
*{box-sizing:border-box;margin:0;padding:0}
html,body{width:727px;height:1200px;overflow:hidden;background:var(--white)}
body{position:relative;font-family:"Arimo",Arial,sans-serif;color:var(--text);font-size:8px}
.abs{position:absolute}

/* header */
.brand{left:50px;top:38px;font-family:"Arimo",Arial,sans-serif;font-weight:700;font-size:22px;letter-spacing:1px;color:var(--text);line-height:1}
.cart{left:473px;top:40px;height:23px;width:202px;border:1px solid var(--line);border-radius:12px;display:flex;align-items:center;font-size:8.5px;color:var(--muted);box-shadow:0 1px 2px rgba(0,0,0,.08)}
.cart-icon{width:24px;height:24px;border-radius:50%;background:var(--purple);margin-left:-2px;display:flex;align-items:center;justify-content:center}
.cart span{margin-left:10px}
.cart .sep{color:#bbb}

/* nav */
.nav{left:0;top:88px;width:727px;height:24px;background:linear-gradient(#6a4a38,var(--leather) 50%,#4f3628)}
.nav a{position:absolute;top:0;height:24px;line-height:24px;color:var(--white);font-size:9.5px;text-decoration:none;text-align:center}
.nav .active{left:48px;width:58px;background:var(--leather-dark)}
.nav .account{left:534px;width:72px;background:var(--beige)}
.nav .referral{left:606px;width:69px;background:var(--purple)}
.crumb{left:50px;top:120px;font-size:7.5px;color:#555}

/* sidebar */
.filter{left:48px;width:174px;border:1px solid var(--line);background:var(--white)}
.filter h3{background:var(--grey-bg);font-family:"Lora",Georgia,serif;font-style:italic;font-weight:400;font-size:10px;color:#666;padding:4px 9px;height:21px}
.filter ul{list-style:none;padding:2px 7px}
.filter li{border-bottom:1px solid #eee;height:17.5px;line-height:17.5px;font-size:7.5px;padding-left:14px;position:relative}
.filter li:last-child{border-bottom:none}
.filter li::before{content:"›";position:absolute;left:2px;color:#999;font-size:9px}

.promo{left:48px;width:174px;height:67px;color:var(--white);overflow:hidden}
.promo h4{font-family:"Lora",Georgia,serif;font-weight:400;font-size:13px}
.promo p{font-size:7px;line-height:1.45;margin-top:3px}
.promo-art{position:absolute;border-radius:6px}
.signup{background:var(--blue)}
.sales{background:var(--beige)}
.services{background:var(--purple)}

/* banner */
.hero{left:229px;top:133px;width:446px;height:128px;background:linear-gradient(90deg,#080808,#202020 55%,#3a3a3a 80%,#1a1a1a)}
.hero-photo{position:absolute;right:40px;top:0;width:110px;height:128px;background:linear-gradient(#4a4a4a,#222)}
.hero h2{position:absolute;left:20px;top:46px;font-family:"Lora",Georgia,serif;font-weight:400;font-size:17px;color:var(--white)}
.hero p{position:absolute;left:113px;top:74px;font-family:"Lora",Georgia,serif;font-size:9px;color:#ddd}

/* products */
.card{width:119px;height:151px;border:1px solid var(--line);background:var(--white)}
.card-photo{position:absolute;left:6px;top:8px;width:105px;height:78px;background:radial-gradient(ellipse at center,#5a5a5a 0,#3a3a3a 25%,#f2f2f2 55%,#fff 70%)}
.card-photo.light{background:radial-gradient(ellipse at center,#e6e6e6 0,#cfcfcf 25%,#f5f5f5 55%,#fff 70%)}
.card-title{position:absolute;left:6px;top:100px;width:108px;font-size:6.5px;line-height:1.3;color:#555}
.price{position:absolute;left:6px;top:134px;width:33px;height:11px;border-radius:3px;background:var(--purple);color:var(--white);font-size:6.5px;line-height:11px;text-align:center}
.details{position:absolute;right:6px;top:134px;width:30px;height:11px;border-radius:3px;background:var(--blue);color:var(--white);font-size:6.5px;line-height:11px;text-align:center}

.pager{left:229px;top:933px;width:446px;height:21px;background:var(--grey-bg);font-size:7.5px;line-height:21px}
.pager .pages{position:absolute;left:10px}
.pager .pages span{margin-right:11px}
.pager .pages b{color:#222;margin-right:11px}
.pager .info{position:absolute;right:10px}
.pager .info i{font-style:normal;margin:0 7px}

/* reassurance */
.info-box{top:1002px;height:59px;border:1px solid var(--line);border-radius:5px;box-shadow:0 1px 2px rgba(0,0,0,.06)}
.info-box h5{position:absolute;left:26px;top:8px;font-family:"Lora",Georgia,serif;font-style:italic;font-weight:700;font-size:8.5px;color:#333}
.info-box .ico{position:absolute;left:8px;top:6px}
.info-box .rule{position:absolute;left:6px;right:6px;top:24px;border-top:1px solid #eee}
.info-box p{position:absolute;left:0;right:0;top:34px;text-align:center;font-size:7px;line-height:1.4;color:#555}
.card-chip{display:inline-block;width:26px;height:15px;border:1px solid #ccc;border-radius:2px;margin-right:3px}
.phone-pill{display:inline-block;background:#ddd;border-radius:8px;padding:1px 10px 1px 22px;font-size:7px;position:relative}
.phone-pill::before{content:"";position:absolute;left:0;top:0;width:16px;height:100%;border-radius:8px;background:#999}

.blog{left:48px;top:1081px;width:301px;height:62px;border:1px solid var(--line);border-radius:5px}
.blog h5{position:absolute;left:28px;top:7px;font-family:"Lora",Georgia,serif;font-style:italic;font-weight:700;font-size:8.5px;color:#333}
.blog .thumb{position:absolute;left:10px;top:28px;width:42px;height:26px;background:linear-gradient(#c8b4c6,#8e6e8c)}
.blog p{position:absolute;left:60px;top:28px;width:230px;font-size:6.5px;line-height:1.35;color:#555}

.social{left:366px;width:309px;height:21px;border-radius:11px;background:linear-gradient(var(--blue),#7aa3cc);color:var(--white);font-size:8.5px;line-height:21px;padding-left:12px}
.social b{font-size:10px}
.social .btn{position:absolute;right:2px;top:2px;width:54px;height:17px;border-radius:9px;background:var(--white);color:var(--blue);text-align:center;line-height:17px;font-size:8px;letter-spacing:.5px}

.footer{left:0;top:1164px;width:727px;height:36px;background:linear-gradient(#5e4231,var(--leather-dark));color:var(--white);font-size:8px;line-height:36px}
.footer .left{position:absolute;left:65px}
.footer .right{position:absolute;right:58px}
.footer .left i{font-style:normal;margin:0 9px}
.footer .right span{margin-left:22px}
</style>
</head>
<body>

<header>
  <div class="abs brand">SANGLEA</div>
  <div class="abs cart">
    <div class="cart-icon"><svg width="12" height="10" viewBox="0 0 12 10"><rect x="1" y="3" width="10" height="6" rx="1" fill="none" stroke="#fff" stroke-width="1.2"/><path d="M3 3V2a3 2 0 0 1 6 0v1" fill="none" stroke="#fff"/></svg></div>
    <span style="margin-left:14px">0,00 $</span><span class="sep">|</span><span>Shopping Basket</span><span class="sep">|</span><span>Checkout</span>
  </div>
</header>

<nav class="abs nav">
  <a class="active" href="#">HOMME</a>
  <a href="#" style="left:130px;width:40px">FEMME</a>
  <a href="#" style="left:200px;width:70px">ACCESSOIRES</a>
  <a class="account" href="#">MON COMPTE</a>
  <a class="referral" href="#">PARRAINAGE</a>
</nav>
<div class="abs crumb">Home &gt; Product List</div>

<aside>
  <section class="abs filter" style="top:133px">
    <h3>Prix</h3>
    <ul><li>0-10 euros</li><li>10-20 euros</li><li>20-30 euros</li><li>30-40 euros</li><li>40-50 euros</li></ul>
  </section>
  <section class="abs filter" style="top:257px">
    <h3>Matiere</h3>
    <ul><li>Synthetique</li><li>Croute de cuir</li><li>Cuir</li><li>Synthetique</li><li>Croute de cui</li></ul>
  </section>
  <section class="abs filter" style="top:382px">
    <h3>Taille</h3>
    <ul><li>85 cm</li><li>90cm</li><li>95cm</li><li>100cm</li></ul>
  </section>

  <section class="abs promo signup" style="top:488px">
    <div class="promo-art" role="img" aria-label="Illustration d'enveloppes de newsletter" style="left:8px;top:14px;width:30px;height:24px;background:linear-gradient(#f1d36a,#5aa0d0)"></div>
    <div class="abs" style="left:48px;top:4px;width:122px">
      <h4>Email Sign Up</h4>
      <p>To receive our exclusive offers and latest product news!</p>
    </div>
    <div class="abs" style="left:14px;top:48px;width:150px;height:13px;background:var(--white);border-radius:7px;font-size:6.5px;color:#666;line-height:13px;padding-left:6px">Enter your email
      <span class="abs" style="right:0;top:0;width:38px;height:13px;border-radius:7px;background:var(--purple);color:var(--white);text-align:center">Signup</span></div>
  </section>

  <section class="abs promo sales" style="top:561px">
    <div class="promo-art" role="img" aria-label="Photo d'un porte-clés en cuir" style="left:6px;top:6px;width:58px;height:55px;border-radius:50%;background:radial-gradient(circle,#8a5a3a,#5b3a26 60%,#b8a58e 72%)"></div>
    <div class="abs" style="left:76px;top:6px;width:96px">
      <h4>Vente &nbsp;Prives</h4>
      <p>To receive our exclusive offers and latest</p>
    </div>
    <div class="abs" style="left:118px;top:50px;width:48px;height:13px;background:var(--leather-dark);color:var(--white);font-size:7px;line-height:13px;text-align:center;border-radius:2px">view offers</div>
  </section>

  <section class="abs promo services" style="top:635px">
    <div class="abs" style="left:10px;top:12px;width:90px">
      <h4>Services</h4>
      <p>To receive our exclusive ListsTo receive our</p>
    </div>
    <div class="promo-art" role="img" aria-label="Illustration d'une mallette de services" style="left:104px;top:12px;width:56px;height:46px;background:linear-gradient(#d77a30,#9a4a18)"></div>
    <svg class="abs" style="left:144px;top:40px" width="22" height="22" viewBox="0 0 22 22"><circle cx="11" cy="11" r="10" fill="#2f7ec4" stroke="#fff" stroke-width="1.5"/><rect x="10" y="9" width="2.4" height="8" fill="#fff"/><circle cx="11.2" cy="6" r="1.4" fill="#fff"/></svg>
  </section>
</aside>

<main>
  <section class="abs hero">
    <div class="hero-photo" role="img" aria-label="Photo d'un homme en manteau sombre portant une ceinture"></div>
    <h2>Les nouvelles collections</h2>
    <p>deja chez sanglea.com!</p>
  </section>

  <article class="abs card" style="left:229px;top:271px"><div class="card-photo light" role="img" aria-label="Ceinture blanche à boucle argentée"></div><p class="card-title">Ceinture Réversible et Ajustable boucle Simple Nord Alto</p><span class="price">46.95€</span><span class="details">Details</span></article>
  <article class="abs card" style="left:393px;top:271px"><div class="card-photo" role="img" aria-label="Ceinture noire à boucle argentée"></div><p class="card-title">Ceinture Réversible et Ajustable boucle Simple Nord Alto</p><span class="price">46.95€</span><span class="details">Details</span></article>
  <article class="abs card" style="left:556px;top:271px"><div class="card-photo" role="img" aria-label="Ceinture noire à boucle plaque"></div><p class="card-title">Ceinture Réversible et Ajustable boucle Simple Nord Alto</p><span class="price">46.95€</span><span class="details">Details</span></article>

  <article class="abs card" style="left:229px;top:434px"><div class="card-photo" role="img" aria-label="Ceinture noire à boucle dorée"></div><p class="card-title">Ceinture Réversible et Ajustable boucle Simple Nord Alto</p><span class="price">46.95€</span><span class="details">Details</span></article>
  <article class="abs card" style="left:393px;top:434px"><div class="card-photo" role="img" aria-label="Ceinture noire à boucle plaque argentée"></div><p class="card-title">Ceinture Réversible et Ajustable boucle Simple Nord Alto</p><span class="price">46.95€</span><span class="details">Details</span></article>
  <article class="abs card" style="left:556px;top:434px"><div class="card-photo" role="img" aria-label="Ceinture noire à boucle ardillon"></div><p class="card-title">Ceinture Réversible et Ajustable boucle Simple Nord Alto</p><span class="price">46.95€</span><span class="details">Details</span></article>

  <article class="abs card" style="left:229px;top:598px"><div class="card-photo light" role="img" aria-label="Ceinture blanche à boucle argentée"></div><p class="card-title">Ceinture Réversible et Ajustable boucle Simple Nord Alto</p><span class="price">46.95€</span><span class="details">Details</span></article>
  <article class="abs card" style="left:393px;top:598px"><div class="card-photo" role="img" aria-label="Ceinture noire à boucle argentée"></div><p class="card-title">Ceinture Réversible et Ajustable boucle Simple Nord Alto</p><span class="price">46.95€</span><span class="details">Details</span></article>
  <article class="abs card" style="left:556px;top:598px"><div class="card-photo" role="img" aria-label="Ceinture noire à boucle plaque"></div><p class="card-title">Ceinture Réversible et Ajustable boucle Simple Nord Alto</p><span class="price">46.95€</span><span class="details">Details</span></article>

  <article class="abs card" style="left:229px;top:764px"><div class="card-photo" role="img" aria-label="Ceinture noire à boucle ardillon"></div><p class="card-title">Ceinture Réversible et Ajustable boucle Simple Nord Alto</p><span class="price">46.95€</span><span class="details">Details</span></article>
  <article class="abs card" style="left:393px;top:764px"><div class="card-photo" role="img" aria-label="Ceinture noire à boucle carrée"></div><p class="card-title">Ceinture Réversible et Ajustable boucle Simple Nord Alto</p><span class="price">46.95€</span><span class="details">Details</span></article>
  <article class="abs card" style="left:556px;top:764px"><div class="card-photo" role="img" aria-label="Ceinture noire enroulée à boucle argentée"></div><p class="card-title">Ceinture Réversible et Ajustable boucle Simple Nord Alto</p><span class="price">46.95€</span><span class="details">Details</span></article>

  <nav class="abs pager">
    <span class="pages"><b>1</b><span>2</span><span>3</span><span>4</span><span>5</span></span>
    <span class="info">Page 1 sur 5<i>|</i>Voir tous les articles</span>
  </nav>
</main>

<section>
  <div class="abs info-box" style="left:48px;width:156px">
    <svg class="ico" width="12" height="14" viewBox="0 0 12 14"><rect x="1" y="6" width="10" height="7" rx="1" fill="#333"/><path d="M3 6V4a3 3 0 0 1 6 0v2" fill="none" stroke="#333" stroke-width="1.5"/></svg>
    <h5>Paiement CB + Payvia</h5><div class="rule"></div>
    <p style="top:32px"><span class="card-chip" style="background:#1a3f8f"></span><span class="card-chip" style="background:#e8a23a"></span><span class="card-chip" style="background:#d9e6f4"></span><span class="card-chip" style="background:#eee"></span></p>
  </div>
  <div class="abs info-box" style="left:210px;width:145px">
    <svg class="ico" width="16" height="12" viewBox="0 0 16 12"><rect x="0" y="1" width="10" height="8" fill="#333"/><path d="M10 4h3l3 3v2h-6z" fill="#333"/><circle cx="3" cy="10" r="1.6" fill="#333"/><circle cx="12" cy="10" r="1.6" fill="#333"/></svg>
    <h5>Livraison</h5><div class="rule"></div>
    <p>Votre commande expédiée sous 24h</p>
  </div>
  <div class="abs info-box" style="left:370px;width:145px">
    <svg class="ico" width="14" height="14" viewBox="0 0 14 14"><path d="M3 1l2 3-1.5 1.5a8 8 0 0 0 5 5L10 9l3 2-1.5 2.5C6 13 1 8 .5 2.5z" fill="#333"/></svg>
    <h5>Service client</h5><div class="rule"></div>
    <p style="top:30px"><span class="phone-pill">06 12 34 56 78</span><br>Service client téléphone et email</p>
  </div>
  <div class="abs info-box" style="left:530px;width:145px">
    <svg class="ico" width="12" height="14" viewBox="0 0 12 14"><circle cx="6" cy="4" r="3" fill="#333"/><rect x="2" y="8" width="8" height="6" fill="#333"/></svg>
    <h5>Garantie</h5><div class="rule"></div>
    <p>Garantie 10 jours "Satisfait<br>ou Remboursé"</p>
  </div>

  <div class="abs blog">
    <span class="abs" style="left:9px;top:6px;width:12px;height:12px;background:#555;border-radius:2px"></span>
    <h5>Derniers articles du blog</h5>
    <div class="thumb" role="img" aria-label="Vignette d'article de blog"></div>
    <p>Lorem Ipsum is simply dummy text of the printing and typesetting industry. Lorem Ipsum has been the industry's standard dummy text ever since the 1500s, when an unknown printer took</p>
  </div>

  <div class="abs social" style="top:1086px">Join us on <b>Cerclia</b><span class="btn">JOIN</span></div>
  <div class="abs social" style="top:1120px">Follow us on <b>Pépia</b><span class="btn">FOLLOW</span></div>
</section>

<footer class="abs footer">
  <span class="left">CGV<i>|</i>CGU<i>|</i>Plan du site</span>
  <span class="right">© Sanglea<span>Contact Us</span><span>Privacy Policy</span></span>
</footer>

</body>
</html>
```